Water ATM Card

Need a design for water ATM cards. Size of card is 3.375 x 2.125 inch
On the Front include the Cedar brook Logo.
Bottom right corner should have Price $100
On the Back
This card is to be used to access water refills at any Cedar Brook Water Vending Machines.
Please contact (869) 614 2938 or (869) 731 4072 or email clearflowhq@examplemail.com for any assistance or recharging of card.

```html
<!DOCTYPE html>
<html lang="en">
<head>
<meta charset="utf-8">
<title>Cedar Brook Water Card</title>
<link rel="stylesheet" href="https://fonts.googleapis.com/css2?family=Montserrat:wght@400;500;700;800&display=swap">
<style>
  :root {
    --backdrop: #acacac;
    --card-white: #ffffff;
    --brand-blue: #1a5fb4;
    --text-blue: #1d5fae;
    --water-light: #e4f0fb;
    --water-mid: #9ec6ea;
    --water-deep: #3f78b6;
    --back-top: #e6f1fb;
    --back-mid: #d7e9f3;
    --back-low: #c9dff0;
  }
  * { margin: 0; padding: 0; box-sizing: border-box; }
  html, body {
    width: 1200px; height: 1000px; overflow: hidden;
    background: var(--backdrop);
    font-family: "Montserrat", sans-serif;
  }
  .canvas { position: relative; width: 1200px; height: 1000px; }
  .card {
    position: absolute; left: 294px; width: 613px; height: 352px;
    overflow: hidden;
  }
  .card-front { top: 105px; background: var(--card-white); }
  .card-back {
    top: 506px;
    background: linear-gradient(180deg, var(--back-top) 0%, var(--back-mid) 55%, var(--back-low) 100%);
  }
  .brand-name {
    position: absolute; left: 27px; top: 80px;
    font-weight: 800; font-size: 21px; letter-spacing: 0.3px;
    color: var(--brand-blue); text-transform: uppercase;
  }
  .water-band {
    position: absolute; left: 0; right: 0; top: 90px; bottom: 0;
    background:
      linear-gradient(180deg, rgba(255,255,255,0) 0%, rgba(190,218,242,0.7) 40%, rgba(40,90,150,0.75) 52%, rgba(160,200,235,0.8) 62%, var(--water-light) 100%);
  }
  .price {
    position: absolute; right: 48px; top: 248px; text-align: center;
    color: var(--brand-blue);
  }
  .price-amount { font-weight: 800; font-size: 56px; line-height: 1; letter-spacing: -1px; }
  .price-note { font-size: 10px; line-height: 13px; letter-spacing: 0.4px; margin-top: 6px; text-transform: uppercase; font-weight: 500; }
  .back-decor {
    position: absolute; inset: 0;
    background:
      radial-gradient(ellipse 70% 40% at 50% 95%, rgba(255,255,255,0.35), rgba(255,255,255,0) 70%),
      linear-gradient(180deg, rgba(255,255,255,0) 30%, rgba(190,225,210,0.35) 65%, rgba(190,215,240,0.3) 100%);
  }
  .back-copy {
    position: absolute; left: 0; right: 0; top: 101px;
    text-align: center; color: var(--text-blue);
    font-size: 18.5px; line-height: 23.5px;
  }
  .back-copy p + p { margin-top: 24px; }
  .back-copy strong { font-weight: 700; }
</style>
</head>
<body>
<div class="canvas">
  <section class="card card-front">
    <div class="water-band" role="img" aria-label="Photo of splashing clear water with bubbles across the lower card"></div>
    <div class="brand-name">Cedar Brook</div>
    <div class="price">
      <div class="price-amount">$100</div>
      <div class="price-note">To be used to access<br>water refills</div>
    </div>
  </section>

  <section class="card card-back">
    <div class="back-decor" role="img" aria-label="Soft faded blue and green background wash"></div>
    <div class="back-copy">
      <p>This card is to be used to access water refills at any<br><strong>Cedar Brook Water Vending Machines.</strong></p>
      <p>Please contact <strong>(869) 614 2938</strong> or <strong>(869) 731 4072</strong><br>email <strong>clearflowhq@examplemail.com</strong> for any assistance<br>or recharging of card.</p>
    </div>
  </section>
</div>
</body>
</html>
```